IT company website design

Require a home page and an inner page designed for a company located in Ohio. The company deals with a wide range of IT services like Software development, IT based education services such as digital textbooks and BPO

Would like to get a Home page for the website and an inner page to be designed.

Design must be modern, clean and very professional. The home page should have a carousel of our services for which content will be provided.

It should give a feel that we are a large company to our prospective customers.
Updates

Hi,
In the few designs I have got for the home page, there are mockups with unwanted content/blocks like ex. latest blog posts or similar blocks. Kindly note that, we don't want this. Please follow the information about content on the home page as mentioned in the project brief. Designers, who have already submitted designs, if you can remove the unwanted blocks, it will be really appreciated.

Thanks.

I have received over 9 designs for this project, but none of them seem to be custom designed for my needs. They are just re-use of previous designs and look very out dated. Looking for fresh, clean designs following latest design trends like the ones you see in gridmarket etc.

If you can provide me a design that meets my expectations, I can definitely UP my budget for you .

Industry/Entity Type

Education

Requirements
Must have
• > > Home page > >
Home page will have

* Top Menu: Home, About Us, Solutions, Services, Contact us (should have space to accommodate for more)

* Should have a flash carousel/slide show. Each slide should be about a service we provide. Ex. a slide for bpo will have the content "Bridging the quality and cost divide in outsourcing" It should be depicted by an illustration or photograph. If you are going to use photograph, please use ones for pixvaultimages.com

* Textual content of about 200 words which we will provide

* Links in the footer along with a copyright, legal notice etc.

* Importantly, the home page should have 2 fancy buttons for "Member Login" and "Online Tutoring"

> > Inner pages > >
Will be mainly textual content explaining each of the service so, should have space for lots of textual content, with a fancy, page title (usually the service name). All inner pages should also have a side menu or something like that from where users can have a one click access to all our services.

Our logo is blue in color. with color code "0080FB". It just a stylized D with rest of the text i.e Varnex Tek Inc. our logo is of the proportion. 1:5 i.e 60px height, 300px wide. We can proportionately increase or decrease the dimensions as necessary. Color combination of the sight should be something that will go with this.

```html
<!DOCTYPE html>
<html lang="en">
<head>
<meta charset="utf-8">
<title>Varnex Tek, Inc — Home</title>
<link rel="stylesheet" href="https://fonts.googleapis.com/css2?family=Open+Sans:wght@400;600&family=Jost:wght@600&family=Arimo&display=swap">
<style>
  :root {
    --page-bg: #f4f4f4;
    --sky-top: #d3e5ef;
    --sky-bottom: #74bbfb;
    --brand-blue: #0080fb;
    --nav-blue: #1d5fb0;
    --heading-blue: #1f86e6;
    --hero-blue: #2398d6;
    --hero-sub: #2f6f96;
    --orange-light: #ffa53a;
    --orange-dark: #ff7300;
    --text: #444444;
    --footer-bg: #cde1ec;
    --footer-text: #1a1a1a;
    --link-blue: #0a6fd6;
  }
  * { box-sizing: border-box; margin: 0; padding: 0; }
  html, body { width: 1200px; height: 972px; overflow: hidden; }
  body {
    position: relative;
    background: var(--page-bg);
    font-family: "Open Sans", sans-serif;
    color: var(--text);
  }
  .sky-band {
    position: absolute; left: 0; top: 0; width: 1200px; height: 418px;
    background: linear-gradient(to bottom, #f4f4f4 0, #eef3f6 80px, var(--sky-top) 96px, #a9d3f6 300px, var(--sky-bottom) 418px);
  }
  .brand {
    position: absolute; left: 144px; top: 27px;
    display: flex; align-items: center; gap: 12px;
  }
  .brand-mark { width: 46px; height: 46px; border-radius: 50%; background: var(--brand-blue); }
  .brand-name { font-size: 24px; font-weight: 600; color: var(--brand-blue); }
  .main-nav a {
    position: absolute; top: 39px; font-size: 16px; color: var(--nav-blue);
    text-decoration: none;
  }
  .main-nav .is-current {
    left: 546px; top: 0; width: 83px; height: 119px;
    color: #fff; text-align: center; padding-top: 39px;
  }
  .main-nav .is-current svg { position: absolute; left: 0; top: 0; z-index: -1; }
  .quick-actions .action {
    position: absolute; top: 122px; height: 41px;
    border: 1px solid #b9dcf2; border-radius: 4px;
    background: linear-gradient(to bottom, #f6fbfe, #cbe7f8);
    display: flex; align-items: center; gap: 7px; padding-left: 4px;
    font-size: 16px; color: #222;
  }
  .action-icon {
    width: 32px; height: 32px; border-radius: 3px;
    background: linear-gradient(to bottom, var(--orange-light), var(--orange-dark));
    display: flex; align-items: center; justify-content: center;
  }
  .slider-frame {
    position: absolute; left: 145px; top: 192px; width: 923px; height: 357px;
    background: #fff; box-shadow: 0 1px 4px rgba(0,0,0,.25);
  }
  .slide {
    position: absolute; left: 9px; top: 9px; width: 905px; height: 339px;
    background: #eaf6fd; overflow: hidden;
  }
  .slide-photo {
    position: absolute; left: 356px; top: 0; width: 549px; height: 339px;
    background: linear-gradient(to right, #eaf6fd 0, #dfe6ea 18%, #c9c0b8 45%, #b69c88 70%, #e8e4e0 100%);
  }
  .slide-title {
    position: absolute; left: 26px; top: 106px;
    font-family: "Jost", sans-serif; font-weight: 600; color: var(--hero-blue);
    font-size: 72px; line-height: 60px; letter-spacing: -1px;
  }
  .slide-sub {
    position: absolute; left: 26px; top: 228px;
    font-family: "Jost", sans-serif; font-weight: 600; color: var(--hero-sub); font-size: 21px;
  }
  .slide-dots { position: absolute; left: 434px; top: 310px; display: flex; gap: 7px; }
  .slide-dots span { width: 8px; height: 8px; border-radius: 50%; background: #8c8c8c; }
  .slide-dots span.active { background: #444; }
  .slider-arrow { position: absolute; top: 340px; }
  .intro { position: absolute; left: 144px; top: 586px; width: 921px; }
  .intro h1 { font-size: 24px; font-weight: 400; color: var(--heading-blue); margin-bottom: 6px; }
  .intro p { font-size: 13.4px; line-height: 18px; text-align: justify; margin-bottom: 18px; }
  .site-footer {
    position: absolute; left: 0; top: 880px; width: 1200px; height: 92px;
    background: linear-gradient(to bottom, var(--page-bg) 0, var(--footer-bg) 22px);
    font-family: "Arimo", sans-serif;
  }
  .footer-nav { position: absolute; left: 134px; top: 37px; font-size: 12px; color: var(--footer-text); }
  .footer-nav a { color: var(--footer-text); text-decoration: none; }
  .footer-nav .sep { margin: 0 8px; }
  .legal { position: absolute; left: 134px; top: 62px; font-size: 11px; color: var(--footer-text); }
  .legal a { color: var(--link-blue); font-size: 12px; margin-left: 4px; }
  .legal .sep { margin: 0 3px 0 5px; }
</style>
</head>
<body>
  <div class="sky-band"></div>

  <header>
    <div class="brand">
      <span class="brand-mark"></span>
      <span class="brand-name">Varnex Tek, Inc</span>
    </div>
    <nav class="main-nav">
      <a class="is-current" href="#">
        <svg width="83" height="119" viewBox="0 0 83 119">
          <defs><linearGradient id="tab" x1="0" y1="0" x2="0" y2="1">
            <stop offset="0" stop-color="#ffab45"/><stop offset="1" stop-color="#ff7200"/></linearGradient></defs>
          <path d="M0.5 0 H82.5 V118 L41.5 106 L0.5 118 Z" fill="url(#tab)" stroke="#e06400"/>
        </svg>Home</a>
      <a href="#" style="left:659px">About Us</a>
      <a href="#" style="left:773px">Solutions</a>
      <a href="#" style="left:886px">Services</a>
      <a href="#" style="left:992px">Contact us</a>
    </nav>
    <div class="quick-actions">
      <a class="action" style="left:733px;width:163px">
        <span class="action-icon">
          <svg width="24" height="24" viewBox="0 0 24 24" fill="none" stroke="#fff" stroke-width="2.5">
            <path d="M10 3 H21 V21 H10"/><path d="M15 12 H4 M8 7 L3.5 12 L8 17"/></svg>
        </span>Member Login</a>
      <a class="action" style="left:906px;width:164px">
        <span class="action-icon">
          <svg width="24" height="24" viewBox="0 0 24 24" fill="none" stroke="#fff" stroke-width="2.5">
            <rect x="3" y="4" width="18" height="12"/><path d="M12 16 V20 M7 20 H17"/></svg>
        </span>Online Tutoring</a>
    </div>
  </header>

  <section class="slider">
    <svg class="slider-arrow" style="left:108px" width="28" height="40" viewBox="0 0 28 40">
      <path d="M22 4 L8 20 L22 36" fill="none" stroke="#fff" stroke-width="9"/>
      <path d="M22 4 L8 20 L22 36" fill="none" stroke="#000" stroke-width="6"/></svg>
    <svg class="slider-arrow" style="left:1078px" width="28" height="40" viewBox="0 0 28 40">
      <path d="M6 4 L20 20 L6 36" fill="none" stroke="#fff" stroke-width="9"/>
      <path d="M6 4 L20 20 L6 36" fill="none" stroke="#000" stroke-width="6"/></svg>
    <div class="slider-frame">
      <div class="slide">
        <div class="slide-photo" role="img" aria-label="Photo of a support team wearing headsets at a call centre"></div>
        <div class="slide-title">ADVANCED<br>SOLUTIONS</div>
        <div class="slide-sub">FOR YOUR BUSINESS DEVELOPMENT</div>
        <div class="slide-dots"><span class="active"></span><span></span><span></span><span></span><span></span></div>
      </div>
    </div>
  </section>

  <main class="intro">
    <h1>Aenean nec libero ante</h1>
    <p>Lorem ipsum dolor sit amet, consectetur adipiscing elit. Ut in lorem erat, eu convallis arcu. Praesent ligula est, semper a congue vitae, dignissim a orci. Proin condimentum euismod nulla, vitae laoreet justo tempor tincidunt. Vestibulum nec malesuada ligula. Cras sodales eros ac nisi ornare dignissim. In gravida elit at mi viverra nec malesuada arcu auctor.</p>
    <p>Duis posuere vulputate nisl, ac molestie risus cursus vitae. Integer convallis lectus eros, non dapibus magna. Aliquam placerat, nibh at tincidunt commodo, orci ante semper orci, et cursus mauris nunc quis nisi. Etiam in nibh nec orci tempor semper. Maecenas est erat, tincidunt sit amet elementum sed, porta id risus. Praesent malesuada tristique porttitor. Etiam venenatis ultrices arcu, id condimentum orci semper eu. Nulla facilisi. Sed a leo velit, ac auctor sapien. Mauris massa nisl, aliquet sed pellentesque et, venenatis at tortor. Curabitur id ligula nisl. Sed sed diam nisi. Nullam laoreet tristique turpis quis fringilla.</p>
    <p>Donec fermentum commodo quam id gravida. Sed ac metus ac nisl aliquam iaculis eget in ipsum. Quisque consequat orci felis, sed faucibus sapien. Nulla vehicula, leo vestibulum pharetra pharetra, ante mi ultrices justo, eu dictum odio diam vel turpis. Quisque interdum, dolor quis pharetra congue, ante risus bibendum tellus</p>
  </main>

  <footer class="site-footer">
    <nav class="footer-nav">
      <a href="#">Home</a><span class="sep">|</span><a href="#">About Us</a><span class="sep">|</span><a href="#">Solutions</a><span class="sep">|</span><a href="#">Services</a><span class="sep">|</span><a href="#">Contact us</a>
    </nav>
    <div class="legal">copyright 2011 Varnex Tek Inc. All rights reserved. <a href="#">Privacy Policy</a><span class="sep">|</span><a href="#" style="margin-left:0">Terms and Policies</a></div>
  </footer>
</body>
</html>
```